Granite Surface Works, Inc. Business Card

New business, we do epoxy, polishing concrete, underlayment, fluid applied flooring, sound proofing, double sided, will need 3 sets of cards with 3 different names and phone numbers.
Company: Granite Surface Works, Inc.
Address and Phone: 6339 Charlotte Pike PMB 2183Nashville, TN 37209
(615) 384-7190
www.granitesurfaceworks.example

Target Market(s)

General Contractors, Contractors, Architects

Contact Information for Business Card

1st Card: Derek Halvorsen C. 708.214.8573 e. derek@granitesurfaceworks.example
Vice President
2nd Card: Morgan Brasfield C. 708.361.5847 e. morgan@granitesurfaceworks.example
President
3rd Card: Raj Oti C. 405.617.3328 e. raj@granitesurfaceworks.example
Managing Partner

Font styles to use
Serif
Sans Serif

Requirements
Must have
• Professional Clean Design, Implement colors from Logo or nicely contrasting
Nice to have
• N/A

```html
<!DOCTYPE html>
<html lang="en">
<head>
<meta charset="utf-8">
<title>Granite Surface Works, Inc. Business Card</title>
<link rel="stylesheet" href="https://fonts.googleapis.com/css2?family=Arimo:wght@400;700&family=Montserrat:wght@700&display=swap">
<style>
  :root {
    --stage: #101011;
    --card: #2a2b2d;
    --card-back: #262729;
    --edge-green: #6b9b3a;
    --brand-blue: #1b6fc6;
    --text-light: #e6e7e8;
    --text-soft: #c4c6c8;
    --rule: rgba(255,255,255,0.08);
  }
  * { box-sizing: border-box; margin: 0; padding: 0; }
  html, body {
    width: 1200px; height: 820px; overflow: hidden;
    background: var(--stage);
    font-family: "Arimo", Arial, sans-serif;
  }
  .card {
    position: absolute; top: 256px;
    width: 540px; height: 309px;
    border-radius: 3px;
    box-shadow: -3px 3px 0 var(--edge-green), 0 18px 40px rgba(0,0,0,0.6);
  }
  .card--front { left: 40px; background: var(--card); }
  .card--back  { left: 620px; background: var(--card-back); overflow: hidden; }

  .brand {
    position: absolute; top: 52px; right: 34px;
    display: flex; align-items: center; gap: 12px;
  }
  .brand__square { width: 30px; height: 30px; background: var(--brand-blue); }
  .brand__name {
    font-family: "Arimo", Arial, sans-serif; font-weight: 400;
    font-size: 25px; color: var(--text-light); letter-spacing: 0.2px;
  }

  .divider {
    position: absolute; top: 148px; left: 150px; right: 30px;
    height: 1px; background: var(--rule);
  }

  .address {
    position: absolute; top: 166px; right: 36px;
    text-align: right; font-size: 13.5px; line-height: 1.35;
    color: var(--text-soft);
  }

  .person { position: absolute; top: 168px; left: 40px; }
  .person__name {
    font-family: "Montserrat", Arial, sans-serif; font-weight: 700;
    font-size: 17px; color: var(--brand-blue); text-transform: uppercase;
  }
  .person__role, .person__cell {
    font-size: 14px; color: var(--text-soft); line-height: 1.4;
  }

  .contact-list { position: absolute; top: 238px; left: 40px; list-style: none; }
  .contact-list li {
    display: flex; align-items: center; gap: 10px;
    font-size: 14px; color: var(--text-light); line-height: 1.45;
  }
  .contact-list svg { width: 13px; height: 13px; flex: none; }

  .back__decoration {
    position: absolute; left: 60px; top: 70px; width: 330px; height: 239px;
    background: linear-gradient(160deg, #3a3b3d 0%, #4a4b4d 55%, #2e2f31 100%);
  }
  .back__brand {
    position: absolute; top: 60px; right: 32px;
    font-size: 25px; color: var(--text-light);
  }
</style>
</head>
<body>
  <section class="card card--front" aria-label="Business card front">
    <div class="brand">
      <span class="brand__square" aria-hidden="true"></span>
      <span class="brand__name">Granite Surface Works</span>
    </div>
    <div class="divider"></div>
    <address class="address">
      4817 Willowmere Road<br>
      PMB 5046 Nashville<br>
      TN 37209
    </address>
    <div class="person">
      <p class="person__name">Derek Halvorsen</p>
      <p class="person__role">Vice President</p>
      <p class="person__cell">708.214.8573</p>
    </div>
    <ul class="contact-list">
      <li>
        <svg viewBox="0 0 16 16" aria-hidden="true"><path fill="#1b6fc6" d="M3.5 1.5l2.5 3-1.5 1.5c.8 1.9 2.2 3.3 4 4l1.5-1.5 3 2.5-1.5 2.5C6.5 13.5 2.5 9.5 1 4z"/></svg>
        (615) 384-7190
      </li>
      <li>
        <svg viewBox="0 0 16 16" aria-hidden="true"><rect x="1" y="3" width="14" height="10" fill="#1b6fc6"/><path d="M1 3l7 6 7-6" fill="none" stroke="#2a2b2d" stroke-width="1.3"/></svg>
        derek@granitesurfaceworks.example
      </li>
      <li>
        <svg viewBox="0 0 16 16" aria-hidden="true"><g fill="none" stroke="#1b6fc6" stroke-width="1.4"><circle cx="8" cy="8" r="6.5"/><ellipse cx="8" cy="8" rx="3" ry="6.5"/><path d="M1.5 8h13"/></g></svg>
        www.granitesurfaceworks.example
      </li>
    </ul>
  </section>

  <section class="card card--back" aria-label="Business card back">
    <div class="back__decoration" role="img" aria-label="Large faint brand symbol decoration in dark grey tones"></div>
    <p class="back__brand">Granite Surface Works</p>
  </section>
</body>
</html>
```